Tarrow Weave Ease Sleep Sofa Hang Tag

I would like to design a 6" x 6", 2-sided, four color hang tag for our sleep sofas. This tag will get attached to the product in the factory before it ships to retailers or consumers. It requires a grommet hole at the center top of the tag. I have attached a powerpoint .pdf of a concept but need you design expertise to make it look outstanding.

Target Market(s)

Furniture retailers and consumers shopping for furniture.

Industry/Entity Type

Home Furniture

Font styles to use
Sans Serif
Other font styles liked:
• Century Gothic

Colors
f04a50
cedeed
f37122

Requirements
Must have
• Contemporary and classic design.
Should not have
• No dark colors.

```html
<!DOCTYPE html>
<html lang="en">
<head>
<meta charset="utf-8">
<title>Tarrow Weave Ease Hang Tag</title>
<link href="https://fonts.googleapis.com/css2?family=Mulish:wght@700;800&family=Questrial&display=swap" rel="stylesheet">
<style>
  :root {
    --backdrop: #5a5a5a;
    --maroon: #8a1c24;
    --taupe: #ab9d8d;
    --ink: #4a4a4a;
    --paper: #ffffff;
  }
  html, body { margin: 0; padding: 0; overflow: hidden; }
  body {
    width: 1200px; height: 1200px;
    background: var(--backdrop);
    font-family: "Questrial", sans-serif;
    color: var(--ink);
    position: relative;
  }
  .tag { position: absolute; top: 330px; width: 540px; height: 540px; }
  .tag--front { left: 40px; }
  .tag--back { left: 620px; }
  .tag-shape { position: absolute; inset: 0; }
  .tag-content { position: absolute; inset: 0; }

  /* front */
  .brand-mark {
    position: absolute; left: 0; right: 0; top: 170px;
    display: flex; align-items: center; justify-content: center; gap: 14px;
    color: var(--maroon); font-size: 34px; letter-spacing: 1px;
  }
  .brand-square { width: 22px; height: 22px; background: var(--maroon); }
  .front-title {
    position: absolute; left: 0; right: 0; top: 320px; text-align: center;
    font-family: "Mulish", sans-serif; font-weight: 800; color: var(--maroon);
    font-size: 27px; letter-spacing: 0.5px;
  }
  .front-subtitle {
    position: absolute; left: 0; right: 0; top: 354px; text-align: center;
    font-size: 26px; color: #555;
  }
  .front-web {
    position: absolute; left: 0; right: 0; top: 428px; text-align: center;
    font-size: 24px; color: #555;
  }

  /* back */
  .band-word {
    position: absolute; top: 112px; color: #fff; font-size: 14px; letter-spacing: 1.5px;
  }
  .band-word--left { right: 316px; }
  .band-word--right { left: 316px; }
  .band-note { position: absolute; top: 140px; font-size: 6px; color: #fff; }
  .band-note--left { right: 330px; }
  .band-note--right { left: 330px; }
  .band-brand {
    position: absolute; left: 230px; top: 92px; width: 76px; height: 58px;
    background: var(--paper); border: 2px solid var(--maroon);
    display: flex; flex-direction: column; align-items: center; justify-content: center; gap: 4px;
    color: var(--maroon); font-size: 12px;
  }
  .band-brand .brand-square { width: 8px; height: 8px; }
  .intro {
    position: absolute; left: 68px; width: 404px; top: 164px; margin: 0;
    font-size: 12.6px; line-height: 16px; text-align: justify;
  }
  .intro strong, .detail strong { color: var(--maroon); font-family: "Mulish", sans-serif; font-weight: 800; }
  .why-bar {
    position: absolute; left: 90px; width: 360px; top: 252px; height: 26px;
    background: var(--maroon); color: #fff; text-align: center;
    font-family: "Mulish", sans-serif; font-weight: 800; font-size: 20px; line-height: 27px;
  }
  .why-sub {
    position: absolute; left: 0; right: 0; top: 280px; text-align: center; font-size: 17px;
  }
  .detail {
    position: absolute; left: 68px; width: 250px; top: 310px;
    font-size: 10.4px; line-height: 12.8px; text-align: justify;
  }
  .detail p { margin: 0; }
  .product-photo {
    position: absolute; left: 328px; top: 312px; width: 144px; height: 118px;
    background: linear-gradient(120deg, #f4f4f2 0%, #dcdcd8 60%, #6e6660 100%);
  }
  .phone {
    position: absolute; left: 0; right: 0; top: 464px; text-align: center;
    font-size: 22px; color: #555;
    display: flex; align-items: center; justify-content: center; gap: 8px;
  }
</style>
</head>
<body>

<svg width="0" height="0" style="position:absolute">
  <defs>
    <path id="tag-outline" d="M90 30 Q150 30 190 50 Q270 0 350 50 Q390 30 450 30 Q510 30 510 90 Q510 150 490 190 Q530 270 490 350 Q510 390 510 450 Q510 510 450 510 Q390 510 350 490 Q270 530 190 490 Q150 510 90 510 Q30 510 30 450 Q30 390 50 350 Q10 270 50 190 Q30 150 30 90 Q30 30 90 30 Z"/>
    <linearGradient id="paper-fill" x1="0" y1="0" x2="0" y2="1">
      <stop offset="0" stop-color="#ffffff"/>
      <stop offset="0.55" stop-color="#e8e8ea"/>
      <stop offset="1" stop-color="#ffffff"/>
    </linearGradient>
    <clipPath id="tag-inner-clip">
      <use href="#tag-outline" transform="translate(270 270) scale(0.965) translate(-270 -270)"/>
    </clipPath>
  </defs>
</svg>

<section class="tag tag--front">
  <svg class="tag-shape" viewBox="0 0 540 540" width="540" height="540">
    <use href="#tag-outline" fill="var(--taupe)"/>
    <use href="#tag-outline" fill="url(#paper-fill)" transform="translate(270 270) scale(0.965) translate(-270 -270)"/>
    <circle cx="270" cy="64" r="19" fill="var(--backdrop)"/>
  </svg>
  <div class="tag-content">
    <div class="brand-mark"><span class="brand-square"></span>Halbrook Furniture</div>
    <div class="front-title">TARROW WEAVE EASE</div>
    <div class="front-subtitle">Sleep Sofa Mattress by Halbrook</div>
    <div class="front-web">www.website.com</div>
  </div>
</section>

<section class="tag tag--back">
  <svg class="tag-shape" viewBox="0 0 540 540" width="540" height="540">
    <use href="#tag-outline" fill="var(--taupe)"/>
    <use href="#tag-outline" fill="url(#paper-fill)" transform="translate(270 270) scale(0.965) translate(-270 -270)"/>
    <rect class="header-band" x="0" y="108" width="540" height="46" fill="var(--taupe)" clip-path="url(#tag-inner-clip)"/>
  </svg>
  <div class="tag-content">
    <span class="band-word band-word--left">handcrafted</span>
    <span class="band-word band-word--right">upholstery</span>
    <span class="band-note band-note--left">to fit your lifestyle</span>
    <span class="band-note band-note--right">since 1944</span>
    <div class="band-brand"><span class="brand-square"></span>Halbrook</div>

    <p class="intro"><strong>Tarrow</strong> provides body-conforming support for personalized comfort and support. The top layer of expertly engineered, high performance visco elastic memory foam is combined with a high-density foam core designed for pressure point relief.</p>

    <div class="why-bar">WHY TARROW ?</div>
    <div class="why-sub">A sleep sofa mattress that rejuvenates !</div>

    <div class="detail">
      <p><strong>Tarrow–</strong> our unique 5-1/2" thick memory foam mattress conforms to your individual body shape and weight for the ultimate of rejuvenating the entire body. The Innovative sleeper mechanism and no cross bar system allows you to enjoy the Maximum comfort of a residential style mattress.</p>
      <p>Tarrow is also hypoallergenic and meets both 16 CFR 1632 and 16 CFR 1633 Federal Flammability Standards.</p>
    </div>
    <div class="product-photo" role="img" aria-label="Photo of a quilted white memory foam mattress corner"></div>

    <div class="phone">
      <svg width="16" height="14" viewBox="0 0 18 16" aria-hidden="true">
        <path d="M2 5 Q9 0 16 5 L14 7 L12 5 L6 5 L4 7 Z" fill="var(--maroon)"/>
        <rect x="3" y="8" width="12" height="7" rx="1.5" fill="var(--maroon)"/>
      </svg>
      123-456-789
    </div>
  </div>
  <svg class="tag-shape" viewBox="0 0 540 540" width="540" height="540" style="pointer-events:none">
    <circle cx="270" cy="64" r="19" fill="var(--backdrop)"/>
  </svg>
</section>

</body>
</html>
```